NOT HAPPY FLYER

The brochure is for a Real Estate Agent, as a prospecting tool for upmarket, expensive homes.

BRIEF:
On the first side will be:
NOT HAPPY? (in a funky font)
(Have a picture of maybe an unhappy dog, or something that displays unhappiness on the front)

The second side:
-With your current service and advice?
Need a result NOW?
-Want a second opinion?

If you have been on the market for over 45 days with no results, it’s time to question why.

Tessa Brindley (photo of Tessa)
Your Modern, Local Real Estate Agent.

It is no secret that the greater the exposure a property has to the market, the greater the number of buyers who are aware of the listing. Every property is unique and Tessa ensures that each property has its own tailored marketing plan, so your property stands out from the crowd.

Whether you’re considering buying locally or internationally, Tessa will work with you to towards understanding those special qualities and those requirements you seek.
If you want to combine these components into an advantageous world class real estate transaction, call Tessa Brindley.

W: (WEBSITE HERE)
M: (MOBILE HERE)
E: (EMAIL HERE)

Target Market(s)

The target market are people who own upmarket, expensive properties.

Industry/Entity Type

Real Estate

Font styles to use
Decorative

Requirements
Must have
• Must be fun, yet professional. Needs to stand out. It will be printed in matt gloss laminate, so it will look very exclusive.

Second side with my photo and a small Hovex logo
Nice to have
• Have some funky fonts.

```html
<!DOCTYPE html>
<html lang="en">
<head>
<meta charset="utf-8">
<title>Not Happy Flyer – Tessa Brindley</title>
<link rel="stylesheet" href="https://fonts.googleapis.com/css2?family=Cabin+Sketch:wght@400;700&family=Nunito:wght@600;700;800&family=Kaushan+Script&display=swap">
<style>
  :root {
    --page: #ffffff;
    --night: #000000;
    --glow: #1fa39a;
    --teal-deep: #0d5f5c;
    --teal: #1b9a94;
    --teal-light: #8fd6d0;
    --ink: #1b2b2c;
    --ink-soft: #2a3a3a;
    --white: #ffffff;
  }
  * { margin: 0; padding: 0; box-sizing: border-box; }
  html, body {
    width: 1200px; height: 1000px; overflow: hidden;
    background: var(--page);
    font-family: "Nunito", Arial, sans-serif;
  }
  .canvas { position: relative; width: 1200px; height: 1000px; }

  /* Front side */
  .front {
    position: absolute; left: 187px; top: 70px; width: 865px; height: 417px;
    background: radial-gradient(ellipse 60% 45% at 50% 105%, #8a8a8a 0%, #2a2a2a 55%, var(--night) 100%);
    border-top: 6px solid #2b2b2b;
    overflow: hidden;
  }
  .front__glow {
    position: absolute; left: 270px; top: 95px; width: 370px; height: 140px;
    background: radial-gradient(ellipse at center, var(--glow) 0%, rgba(31,163,154,0.55) 40%, rgba(0,0,0,0) 72%);
    filter: blur(6px);
  }
  .front__title {
    position: absolute; left: 0; right: 0; top: 138px; text-align: center;
    font-family: "Cabin Sketch", "Comic Sans MS", cursive;
    font-weight: 400; font-size: 42px; letter-spacing: 2px;
    color: var(--white);
  }
  .front__pet {
    position: absolute; left: 258px; top: 232px; width: 350px; height: 185px;
    border-radius: 48% 48% 8% 8% / 60% 60% 6% 6%;
    background: radial-gradient(ellipse at 50% 55%, #3a332c 0%, #6a5d4e 30%, #cbbfac 65%, #e4dbcc 100%);
  }

  /* Back side */
  .back {
    position: absolute; left: 189px; top: 520px; width: 862px; height: 410px;
    background: linear-gradient(180deg, var(--teal-deep) 0%, var(--teal) 38%, var(--teal-light) 58%, var(--white) 72%, var(--white) 100%);
    overflow: hidden;
  }
  .back__lead {
    position: absolute; left: 22px; top: 26px;
    font-family: "Cabin Sketch", "Comic Sans MS", cursive;
    font-weight: 400; font-size: 40px; letter-spacing: 3px; white-space: nowrap;
    color: var(--white);
  }
  .back__portrait {
    position: absolute; left: 0; top: 78px; width: 303px; height: 332px;
    background: radial-gradient(ellipse 45% 55% at 45% 45%, #d9a88c 0%, #8a5a3e 45%, #4e6a48 80%, #a7c4c0 100%);
  }
  .back__content { position: absolute; left: 319px; top: 78px; width: 515px; }
  .headline {
    font-weight: 800; font-size: 31px; line-height: 35px; color: var(--white);
  }
  .subhead {
    margin-top: 12px; font-weight: 800; font-size: 20.5px; line-height: 23px; color: var(--ink);
  }
  .body-copy {
    margin-top: 14px; font-weight: 700; font-size: 10.4px; line-height: 14.5px; color: var(--ink-soft);
  }
  .body-copy + .body-copy { margin-top: 7px; }
  .contacts {
    position: absolute; left: 323px; top: 333px;
    font-weight: 800; font-size: 11.5px; letter-spacing: 0.6px; color: var(--ink);
  }
  .contacts span { margin-right: 8px; }
  .signoff { position: absolute; left: 321px; top: 356px; white-space: nowrap; }
  .signoff__name {
    font-family: "Kaushan Script", cursive; font-size: 20px; color: var(--ink);
  }
  .signoff__tag {
    font-weight: 700; font-size: 17.5px; color: var(--teal); margin-left: 10px;
  }
  .brand {
    position: absolute; left: 778px; top: 305px; width: 56px; height: 72px;
    background: var(--night);
    display: flex; align-items: center; justify-content: center;
    font-weight: 800; font-size: 11px; color: var(--white);
  }
</style>
</head>
<body>
<main class="canvas">
  <section class="front">
    <div class="front__glow"></div>
    <h1 class="front__title">Not Happy?</h1>
    <div class="front__pet" role="img" aria-label="Photo of a sad pug resting its chin on its paws"></div>
  </section>

  <section class="back">
    <p class="back__lead">...with your current service and advice?</p>
    <div class="back__portrait" role="img" aria-label="Portrait photo of agent Tessa Brindley"></div>
    <div class="back__content">
      <h2 class="headline">Need a result NOW?<br>Want a second opinion?</h2>
      <p class="subhead">If you have been on the market for over 45 days<br>with no results, it’s time to question why</p>
      <p class="body-copy">It is no secret that the greater the exposure a property has to the market, the greater the number of buyers who are aware of the listing. Every property is unique and Tessa ensures that each property has its own tailored marketing plan, so your property stands out from the crowd.</p>
      <p class="body-copy">Whether you’re considering buying locally or internationally, Tessa will work with you to towards understanding those special qualities and those requirements you seek. If you want to combine these components into an advantageous world class real estate transaction, call Tessa Brindley.</p>
    </div>
    <p class="contacts"><span>W: (WEBSITE HERE)</span><span>M: (MOBILE HERE)</span><span>E: (EMAIL HERE)</span></p>
    <p class="signoff"><span class="signoff__name">Tessa Brindley</span><span class="signoff__tag">Your Modern, Local Real Estate Agent</span></p>
    <div class="brand">Hovex</div>
  </section>
</main>
</body>
</html>
```